Progressive business consultancy seeking "Accounting Industry Flyer"

We are looking for an industry flyer that we will use with potential clients/prospects that outlines our skills and experience in delivering change across the Accounting Services Industry. The flyer will be used to help potential clients understand the challenges and issues faced by the accounting industry and how our service offerings can help them solve their project challenges and problems.

About Us:
Based in Melbourne, Australia, Vendor-o is a management consulting organisation that partners with their clients to lead the execution of strategic process and system improvement initiatives.

Vendor-o offers business advisory services in Project Management, Business Process Management, Change Management, Business Analysis and Business Intelligence. Vendor-o combines hands on delivery with coaching in best practice methodologies and approaches to build our clients capabilities ensuring their ongoing success in project implementations.

Vendor-o has extensive experience across a wide range of industries. We specialise in assisting organisations across the accounting, legal, financial services and health sectors.

Our core purpose is to help businesses in the middle market navigate transformational change through clear and focused execution and enablement.

www.vendor-o.com.au
@vendor_o

What we're looking for:

A professional, corporate, industry flyer providing an overview of our capabilities and experience in the accounting industry. Focus is on the "e" in vendor-o. The look should be sharp and crisp, with a professional and corporate feel. The target for the flyer is Accountants and Mid-Tier Accounting Firms.

The Vendor-o colours are white and blue (RGB:0/86/162 and
CMYK 97/73/4/0)

A professional, corporate theme that is consistent across both sides of the flyer. The design should reflect our focus on the "e" in vendor-o, which is what we're really about - "e"xecution and "e"nablement of change.

I've attached a PNG file of our word template which shows the focus on the "e" as a watermark on the document as well as the font files if required.

Let me know if you need any further information or design specifics.

Thanks,

Felicity
(on behalf of Gregory)
Updates

Hi All, Thanks for your design submissions so far. We have discovered that our hero image has not been attached to the brief. Please find the jpeg attached now. It has been loaded as "Vendor-o Hero Image.jpg" Thanks Gregory @vendor_o

Reason: Hi Designers, Thanks to everyone who has taken the time to make a submission on our contest. We really appreciate it. We have decided to extend our deadline by 5 days so we can review the designs with other colleagues and provide feedback to everyone who has made a submission. Thanks for all your creative designs. Gregory @vendor_o

Reason: Hi designers, thanks to everyone for taking the time to submit their designs. We are going to have to extend our deadline again as we haven't had an opportunity to review all of the designs properly and provide feedback.

Target Market(s)

Accountants and Accounting Firms (mid tier firms)

Industry/Entity Type

Management Consulting

Font styles to use
Other font styles liked:
• Calibri & Attached font files.

Colors
0455a3
3277b5
ffffff

Requirements
Must have
• A Professional A4 double sided colour flyer consisting of:
• Front Page:
• - hero image (attached)
• - Draft content front (attached)
• - Vendor-o Logo (attached)
• Back Page
• - Draft content back (attached)

```html
<!DOCTYPE html>
<html lang="en">
<head>
<meta charset="utf-8">
<title>Vendor-o Accounting Industry Flyer</title>
<link rel="stylesheet" href="https://fonts.googleapis.com/css2?family=Archivo:wght@700;800&family=Open+Sans:ital,wght@0,300;0,400;0,600;1,400;1,700&display=swap">
<style>
  :root {
    --blue: #1c5be3;
    --blue-deep: #0455a3;
    --blue-soft: #3277b5;
    --white: #ffffff;
    --stage: #e9e4dc;
    --panel: rgba(255,255,255,0.32);
  }
  * { box-sizing: border-box; margin: 0; padding: 0; }
  html, body { width: 1200px; height: 900px; overflow: hidden; }
  body {
    background: var(--stage);
    position: relative;
    font-family: "Open Sans", Calibri, sans-serif;
  }
  .page {
    position: absolute;
    top: 65px;
    height: 768px;
    overflow: hidden;
  }

  /* ---------- Front ---------- */
  .front { left: 47px; width: 550px; background: var(--blue); color: var(--white); }
  .front .shapes { position: absolute; inset: 0; }
  .brand {
    position: absolute;
    font-family: "Open Sans", sans-serif;
    font-weight: 400;
    letter-spacing: 1px;
    line-height: 1;
  }
  .brand-sub {
    position: absolute;
    font-family: "Open Sans", sans-serif;
    font-size: 10px;
    line-height: 1;
  }
  .front .brand { right: 38px; top: 22px; font-size: 50px; color: var(--white); }
  .front .brand-sub { right: 52px; top: 76px; color: var(--white); }

  .hero-image {
    position: absolute;
    left: 245px; top: 92px; width: 280px; height: 236px;
    background: linear-gradient(90deg, rgba(255,255,255,1) 0%, rgba(170,180,196,0.8) 22%, #56647d 55%, #2e3c57 100%);
  }

  .intro { position: absolute; left: 27px; top: 100px; width: 270px; color: var(--blue); }
  .intro h2 { font-family: "Archivo", sans-serif; font-weight: 800; font-size: 11.5px; line-height: 14px; margin-bottom: 1px; }
  .intro p { font-size: 9px; line-height: 14.4px; text-align: justify; margin-bottom: 14px; }

  .challenges { position: absolute; left: 27px; top: 368px; width: 234px; }
  .challenges h2 { font-family: "Archivo", sans-serif; font-weight: 800; font-size: 10.5px; line-height: 12px; margin-bottom: 1px; }
  .challenges p { font-size: 7px; line-height: 11.1px; text-align: justify; letter-spacing: -0.05px; margin-bottom: 10px; }
  .challenges h2.later { margin-top: 4px; }

  .help-panel {
    position: absolute; left: 271px; top: 343px; width: 252px; height: 392px;
    background: var(--panel);
    padding: 10px 9px 0 10px;
  }
  .help-panel h2 { font-family: "Archivo", sans-serif; font-weight: 800; font-size: 10px; line-height: 11.5px; margin-bottom: 3px; }
  .help-panel p { font-size: 7.6px; line-height: 11.7px; margin-bottom: 11px; }
  .help-panel ul { list-style: none; font-size: 7.6px; line-height: 11.7px; margin-bottom: 8px; }
  .help-panel li { padding-left: 9px; text-indent: -9px; }
  .help-panel li::before { content: "•"; display: inline-block; width: 9px; text-indent: 0; }
  .help-panel h3 { font-family: "Archivo", sans-serif; font-weight: 800; font-size: 9px; text-align: center; }
  .help-panel .case { font-style: italic; font-size: 6.2px; line-height: 8.6px; text-align: justify; margin-bottom: 12px; }
  .help-panel .call { font-style: italic; font-weight: 700; font-size: 8.6px; line-height: 12.5px; text-align: center; }

  /* ---------- Back ---------- */
  .back { left: 623px; width: 540px; background: var(--white); }
  .back .shapes { position: absolute; inset: 0; }
  .back .brand { left: 44px; top: 34px; font-size: 82px; color: var(--blue); }
  .back .brand-sub { left: 400px; top: 130px; font-size: 12px; color: var(--blue); }
  .what-we-do {
    position: absolute; left: 0; top: 157px; width: 540px; height: 52px;
    background: var(--blue); color: var(--white);
    font-weight: 300; font-size: 42px; line-height: 52px; padding-left: 54px;
  }
  .service { position: absolute; right: 238px; text-align: right; color: var(--blue); }
  .service h3 { font-family: "Archivo", sans-serif; font-weight: 800; font-size: 16.5px; line-height: 20px; }
  .service p { font-size: 11px; line-height: 16px; }
</style>
</head>
<body>

<section class="page front">
  <svg class="shapes" width="550" height="768" viewBox="0 0 550 768" aria-hidden="true">
    <path d="M0,84 C140,102 300,66 550,82 L550,318 C420,300 250,360 0,350 Z" fill="#ffffff"/>
  </svg>

  <div class="brand">Vendor-o</div>
  <div class="brand-sub">Pty Ltd</div>

  <div class="hero-image" role="img" aria-label="Hero image: business person touching a glowing cloud network of connected technology icons"></div>

  <div class="intro">
    <h2>Who are Vendor-o?</h2>
    <p>Based in Melbourne, Australia, Vendor-o is a management consulting organisation who partner with their clients to lead the execution of strategic process and system improvement initiatives. Our core purpose is to help your business navigate transformational change through clear and focused execution and enablement.</p>
    <p>Vendor-o has proven experience leading change and delivering improvements to organisations across a range of industries. However, we specialise in working with accounting firms in the middle market helping them to navigate the disruptive changes rapidly changing the face of their industry. Our expertise includes business process automation and the management of onshore and offshore teams across tax and audit compliance services.</p>
  </div>

  <div class="challenges">
    <h2>What are the major challenges facing the accounting industry?</h2>
    <p>The three major disruptors facing accounting firms are the offshoring of compliance activities, rapid changes in technology and the internet. These industry wide disruptors are placing pressure on fee negotiations, revenue generation and are also providing a significant increase in competitive activity. As clients continue to push prices down, accounting firms have and/or are in the process of implementing systems and technologies to drive further efficiencies and reduce costs. In addition the outsourcing of accounting services for low end and non-confidential work to further lower client costs has been pervasive. This has now started to extend across end to end tax and audit compliance processes as firms start to recognise the qualified accounting capability they have available to them at a much lower cost.</p>
    <p>The need to win new business and increased competition has resulted in the entry of the Big 4 into the middle tier market and the emergence and expansion of non-traditional competitors with different business models. Cloud computing is enabling businesses to scale at a very rapid rate and maintain low cost operating models. As the industry becomes hyper-competitive it is crucial for accounting firms to deepen their understanding of clients and build their capability to offer value added</p>
    <h2 class="later">What are our capabilities?</h2>
    <p>We offer a range of project advisory services including project management, business process improvement, change management, business analysis and business intelligence. At Vendor-o we aim to build your organisation's capabilities enabling you to manage and execute change initiatives. We do this by providing hands-on project delivery along with coaching in best practice project methodologies. We look to establish simple repeatable project and change management processes that can continue to be utilised by your organisation long into the future.</p>
  </div>

  <div class="help-panel">
    <h2>How we can help professional services firms in the accounting industry</h2>
    <p>Vendor-o have deep industry experience gained across the Big 4 and mid-tier accounting firms and a consistent track record for leading change and delivering improvements to business processes. Our people have extensive industry experience leading and managing teams at organisations such as Northgate Audit, Hollis Brandt, RLK Group, Carrow Accountants, Meridian Advisers and Ashby Partners.</p>
    <p style="margin-bottom:2px">Our delivery model involves us working directly alongside you helping you to:</p>
    <ul>
      <li>Recognise the major disruptors for your business</li>
      <li>Ensure you have developed a clear strategy on how to respond</li>
      <li>Develop a plan and execute the changes required to ensure business growth is maintained and the quality of your client work is not compromised</li>
    </ul>
    <h3>Case Study</h3>
    <p class="case">A leading mid-tier accounting firm required support to implement large scale process and system improvements identified through a major organisational review. Through a structured program delivery approach we harnessed the required internal resources, engaged widely across the organisation and delivered major changes throughout the firm every 8 weeks with minimal disruption to normal business operations. The implementation of these improvements freed up over x hours per annum that could be redirected to value added advisory services.</p>
    <p class="call">Check out our website at www.vendor-o.com.au and contact us on (+61) 3 9555 0142 to help your organisation navigate change and drive successful business outcomes.</p>
  </div>
</section>

<section class="page back">
  <svg class="shapes" width="540" height="768" viewBox="0 0 540 768" aria-hidden="true">
    <path d="M345,207 C378,330 382,560 330,768 L540,768 L540,207 Z" fill="var(--blue)"/>
    <g fill="#ffffff">
      <circle cx="352" cy="260" r="33"/>
      <circle cx="362" cy="360" r="33"/>
      <circle cx="367" cy="460" r="33"/>
      <circle cx="362" cy="563" r="33"/>
      <circle cx="352" cy="663" r="33"/>
    </g>
    <g fill="var(--blue)">
      <circle cx="352" cy="260" r="23"/>
      <circle cx="362" cy="360" r="23"/>
      <circle cx="367" cy="460" r="23"/>
      <circle cx="362" cy="563" r="23"/>
      <circle cx="352" cy="663" r="23"/>
    </g>
    <g fill="#ffffff" stroke="#ffffff" stroke-width="1.2">
      <rect x="348" y="248" width="8" height="7"/>
      <path d="M352,255 V260 M341,260 H363 M341,260 V264 M352,260 V264 M363,260 V264" fill="none"/>
      <rect x="337" y="264" width="8" height="7"/><rect x="348" y="264" width="8" height="7"/><rect x="359" y="264" width="8" height="7"/>
    </g>
    <g fill="#ffffff" stroke="#ffffff" stroke-width="1.2">
      <rect x="356" y="346" width="16" height="11" fill="none"/>
      <circle cx="352" cy="358" r="3"/>
      <path d="M347,372 V365 H357 V372 Z"/>
      <path d="M360,354 L363,350 L366,352 L369,348" fill="none"/>
    </g>
    <g fill="none" stroke="#ffffff" stroke-width="2">
      <path d="M357,452 A11,11 0 0 1 377,455"/>
      <path d="M377,468 A11,11 0 0 1 357,465"/>
      <path d="M374,451 L378,456 L381,450" />
      <path d="M360,469 L356,464 L353,470" />
    </g>
    <g fill="#ffffff" stroke="#ffffff" stroke-width="1.2">
      <rect x="358" y="550" width="15" height="12" fill="none"/>
      <path d="M361,560 V557 M365,560 V554 M369,560 V552"/>
      <circle cx="353" cy="561" r="3"/>
      <path d="M347,575 V568 H359 V575 Z"/>
    </g>
    <g fill="none" stroke="#ffffff" stroke-width="2.4">
      <circle cx="346" cy="656" r="5" stroke-dasharray="2.4 1.6"/>
      <circle cx="359" cy="665" r="6" stroke-dasharray="2.6 1.8"/>
    </g>
  </svg>

  <div class="brand">Vendor-o</div>
  <div class="brand-sub">Pty Ltd</div>

  <div class="what-we-do">What we do</div>

  <div class="service" style="top:237px">
    <h3>Project Management</h3>
    <p>Delivering High Quality Projects on time and<br>within budget.</p>
  </div>
  <div class="service" style="top:341px; right:224px">
    <h3>Business Process Management</h3>
    <p>Engaging your people to understand current prac-<br>tices and develop smarter business processes</p>
  </div>
  <div class="service" style="top:436px; right:214px">
    <h3>Change Management</h3>
    <p>Building engagement through business understand-<br>ing clear communication and relevant capability.</p>
  </div>
  <div class="service" style="top:532px; right:224px">
    <h3>Business Analysis</h3>
    <p>Building innovative links between your depart-<br>ments, driving collaboration and providing holistic<br>business solutions</p>
  </div>
  <div class="service" style="top:632px; right:236px">
    <h3>Business Intelligence</h3>
    <p>Leveraging one of your organizations most<br>valuable assets - your data.</p>
  </div>
</section>

</body>
</html>
```